Weigh Fresh Dwelling Business card

I have had at the logo designed here and attached. The business compares off the plan apartments in Sydney and provides quick comparison for new home buyers e.g price, floor plans and location. I would like the complimentary colours used on the business card. I would like it be unique but also look professional. I also have a website to gain inspiration from www.weighfreshdwelling.com.au
Updates
Industry/Entity Type
Business
Contact Information for Business Card
Lena Vortigan
Director of Business Development
e: lena.vortigan@weighfreshdwelling.com.au
p: (02) 7394 6628
m: 0431 572 908
w: www.weighfreshdwelling.com.au
Look and feel
Each slider illustrates characteristics of the customer's brand and the style your logo design should communicate.

```html
<!DOCTYPE html>
<html lang="en">
<head>
<meta charset="utf-8">
<title>Weigh Fresh Dwelling – Business Card</title>
<link href="https://fonts.googleapis.com/css2?family=Open+Sans:wght@400;600;700&display=swap" rel="stylesheet">
<style>
  :root {
    --backdrop: #e7e4e0;
    --card-light: #ffffff;
    --card-dark: #232323;
    --brand-green: #8cc63f;
    --brand-blue: #2a90d2;
    --ink: #1c1c1c;
    --paper-text: #ffffff;
  }
  * { margin: 0; padding: 0; box-sizing: border-box; }
  html, body {
    width: 1200px; height: 1000px; overflow: hidden;
    background: var(--backdrop);
    font-family: "Open Sans", Arial, sans-serif;
    color: var(--ink);
  }
  .canvas { position: relative; width: 1200px; height: 1000px; }

  .card {
    position: absolute; left: 265px; width: 666px; height: 397px;
    box-shadow: 0 6px 18px rgba(0,0,0,0.25);
    overflow: hidden;
  }
  .card--front { top: 73px; background: var(--card-light); }
  .card--back { top: 532px; background: var(--card-dark); }

  .wordmark {
    position: absolute; display: flex; align-items: center; gap: 12px;
    font-weight: 600; color: var(--brand-green); white-space: nowrap;
  }
  .wordmark__square { background: var(--brand-blue); flex: none; }
  .card--front .wordmark { left: 37px; top: 62px; font-size: 34px; }
  .card--front .wordmark__square { width: 30px; height: 30px; }
  .card--back .wordmark { left: 0; right: 0; top: 158px; justify-content: center; font-size: 46px; }
  .card--back .wordmark__square { width: 40px; height: 40px; }

  .person { position: absolute; left: 33px; top: 186px; }
  .person__name {
    font-size: 18px; font-weight: 700; color: var(--brand-blue);
    text-transform: uppercase; letter-spacing: 0.2px; line-height: 24px;
  }
  .person__role { font-size: 16px; line-height: 22px; }

  .contact-list { position: absolute; left: 33px; top: 254px; list-style: none; }
  .contact-list li {
    display: flex; align-items: center; gap: 8px;
    font-size: 16px; line-height: 23.5px;
  }
  .contact-list svg { width: 14px; height: 14px; flex: none; fill: var(--brand-blue); }

  .address { position: absolute; left: 412px; top: 254px; font-size: 16px; line-height: 22.5px; }

  .accent-bar { position: absolute; bottom: 0; height: 25px; }
  .accent-bar--green { left: 0; width: 352px; background: var(--brand-green); }
  .accent-bar--blue { left: 359px; right: 0; background: var(--brand-blue); }

  .back-url {
    position: absolute; left: 0; right: 0; top: 347px; text-align: center;
    color: var(--paper-text); font-size: 16px; letter-spacing: 2.2px;
  }
</style>
</head>
<body>
<main class="canvas">
  <section class="card card--front">
    <div class="wordmark"><span class="wordmark__square"></span>Weigh Fresh Dwelling</div>

    <div class="person">
      <p class="person__name">Lena Vortigan</p>
      <p class="person__role">Managing Director</p>
    </div>

    <ul class="contact-list">
      <li>
        <svg viewBox="0 0 14 14" aria-hidden="true"><path d="M4 0h6a1 1 0 0 1 1 1v12a1 1 0 0 1-1 1H4a1 1 0 0 1-1-1V1a1 1 0 0 1 1-1zm0.5 2v8h5V2zm2.5 9a1 1 0 1 0 0 2 1 1 0 0 0 0-2z"/></svg>
        + 000 000 0000
      </li>
      <li>
        <svg viewBox="0 0 14 14" aria-hidden="true"><path d="M1 5c0-2 2.5-3 6-3s6 1 6 3v1h-3V4.5H4V6H1zM3 7h8l2 6H1z"/></svg>
        + 000 000 0000
      </li>
      <li>
        <svg viewBox="0 0 14 14" aria-hidden="true"><path d="M0 3h14v8H0zm1 1v.4l6 3.8 6-3.8V4z"/></svg>
        info@weighfreshdwelling.com.au
      </li>
      <li>
        <svg viewBox="0 0 14 14" aria-hidden="true"><path d="M7 0a7 7 0 1 0 0 14A7 7 0 0 0 7 0zm0 1.5c.8 0 1.7 1.7 1.9 4.5H5.1C5.3 3.2 6.2 1.5 7 1.5zM1.6 6h2.1c.1-1.6.4-3 1-4A5.6 5.6 0 0 0 1.6 6zm0 2a5.6 5.6 0 0 0 3.1 4c-.6-1-.9-2.4-1-4zm3.5 0h3.8c-.2 2.8-1.1 4.5-1.9 4.5S5.3 10.8 5.1 8zm5.2 0c-.1 1.6-.4 3-1 4a5.6 5.6 0 0 0 3.1-4zm2.1-2a5.6 5.6 0 0 0-3.1-4c.6 1 .9 2.4 1 4z"/></svg>
        www.weighfreshdwelling.com.au
      </li>
    </ul>

    <address class="address" style="font-style: normal;">
      Level 27, AR Tower 4<br>
      Clarence Street Sydney,<br>
      NSW 2000
    </address>

    <div class="accent-bar accent-bar--green"></div>
    <div class="accent-bar accent-bar--blue"></div>
  </section>

  <section class="card card--back">
    <div class="wordmark"><span class="wordmark__square"></span>Weigh Fresh Dwelling</div>
    <p class="back-url">www.weighfreshdwelling.com.au</p>
  </section>
</main>
</body>
</html>
```